Exclusive beauty salon needs a price list or services booklet

I need a new very attractive flyer for my beauty salon, containing information on the different services and their prices.
In attachment you can find a pdf of the "old" one, but I'd love to have a beautifully designed new one!
I'd love to have a booklet in format 148 x 148 mm, or in US format, containing 12 or 16 pages, but if you can offer other nice looking designs they are welcome!
The services that need to come in the booklet with their prices can all be found on my website: www.atelierkova.be, starting with
Gelaatsverzorging
Wimperverlenging
Suikerontharing
Wimperlifting
Permanente Make Up
Airbrush Tanning

Target Market(s)

woman from 20 to 89 years old

Industry/Entity Type

Beauty Salon

Font styles to use
Sans Serif

Colors

Designer to choose colors to be used in the design.

Requirements
Must have
• a classy nice look, it must contain details about the services from my beauty salon and their prices, and nice pictures.
• The Names, prices and explanations of the services can easily be found on my website: www.atelierkova.be
Nice to have
• In attachment you can find the "old" price list in pdf, what I need now is a "new booklet" with the new logo and updated services price list.
• I need a very nice and attractive looking booklet, classy chique, Paris chique, looking very expensive.
Should not have
• Not too much colors, not too curly, but still feminine

```html
<!DOCTYPE html>
<html lang="en">
<head>
<meta charset="utf-8">
<title>Atelier Kova – Beauty Salon Services &amp; Prices</title>
<link href="https://fonts.googleapis.com/css2?family=Roboto+Condensed:wght@400;700&family=Roboto:wght@400;500;700&display=swap" rel="stylesheet">
<style>
  :root {
    --page: #ffffff;
    --frame: #a9dbea;
    --sky: #a6d7e7;
    --sky-soft: #e9f5f8;
    --tint: #9fcfdf;
    --teal-dark: #2f5f73;
    --ink: #355f70;
    --brand: #8ccbe0;
    --skin-light: #f6e7df;
    --skin-mid: #edd3c6;
    --hair: #8a6656;
  }
  * { margin: 0; padding: 0; box-sizing: border-box; }
  html, body { width: 1200px; height: 637px; overflow: hidden; background: var(--page); }
  body { position: relative; font-family: "Roboto", Arial, sans-serif; }

  .page {
    position: absolute; top: 44px; width: 551px; height: 549px;
    border: 2px solid var(--frame); overflow: hidden; background: var(--page);
  }
  .page--cover { left: 40px; }
  .page--back { left: 601px; }
  .page svg.shapes { position: absolute; inset: 0; width: 100%; height: 100%; }

  /* Cover */
  .cover-photo {
    position: absolute; left: 258px; top: 0; width: 293px; height: 549px;
    background:
      radial-gradient(ellipse 120px 150px at 170px 60px, rgba(138,102,86,0.55), transparent 75%),
      radial-gradient(ellipse 150px 230px at 150px 280px, var(--skin-mid), transparent 80%),
      linear-gradient(180deg, #ffffff 0%, var(--skin-light) 50%, #ffffff 100%);
  }
  .cover-title { position: absolute; left: 36px; top: 154px; }
  .cover-title .kicker {
    font-family: "Roboto Condensed", sans-serif; font-size: 19px; color: #fff; line-height: 1;
  }
  .cover-title h1 {
    font-family: "Roboto Condensed", sans-serif; font-weight: 700; color: var(--teal-dark);
    font-size: 48px; line-height: 0.86; margin-top: 4px; letter-spacing: 0.2px;
  }
  .cover-intro {
    position: absolute; left: 36px; top: 254px; width: 190px;
    border-top: 2px dotted #fff; border-bottom: 2px dotted #fff;
    padding: 8px 0 10px;
    font-size: 7.5px; line-height: 1.45; color: #fff; text-transform: uppercase;
  }
  .brand {
    position: absolute; font-family: "Roboto", sans-serif; font-weight: 400;
    color: var(--brand); letter-spacing: 5px; text-align: center; font-size: 12px;
  }
  .brand .dot { display: block; width: 10px; height: 10px; border-radius: 50%; background: var(--brand); margin: 0 auto 28px; }
  .brand--cover { left: 24px; top: 456px; width: 180px; }

  /* Back */
  .back-photo {
    position: absolute; inset: 0;
    background: linear-gradient(120deg, #c9e4ec 0%, var(--tint) 45%, #b3dbe7 100%);
  }
  .back-note {
    position: absolute; left: 244px; top: 44px; width: 168px; text-align: center;
    font-size: 13px; line-height: 1.32; color: var(--ink);
  }
  .services {
    position: absolute; left: 38px; top: 206px; width: 268px; text-align: center;
    font-size: 10px; line-height: 1.35; color: var(--ink);
  }
  .services dt { font-weight: 700; text-transform: uppercase; letter-spacing: 0.6px; margin-top: 3px; }
  .services dt:first-child { margin-top: 0; }
  .brand--back { left: 358px; top: 240px; width: 170px; }
  .contact { position: absolute; left: 240px; top: 406px; width: 146px; list-style: none; }
  .contact li {
    display: flex; align-items: center; gap: 9px; padding: 4px 0 5px;
    border-bottom: 1px solid rgba(255,255,255,0.7); color: var(--teal-dark);
    font-size: 8px; font-weight: 500;
  }
  .contact li:last-child { border-bottom: none; align-items: flex-start; font-weight: 400; line-height: 1.3; }
  .contact .phone { font-size: 13px; font-weight: 700; border-bottom: none; }
  .contact svg { width: 15px; height: 15px; flex: none; fill: var(--teal-dark); }
</style>
</head>
<body>

<section class="page page--cover">
  <div class="cover-photo" role="img" aria-label="Portrait photo of a smiling woman with dark hair, hand resting on her cheek"></div>
  <svg class="shapes" viewBox="0 0 551 549" aria-hidden="true">
    <polygon points="258,170 420,320 258,320" fill="var(--sky-soft)" opacity="0.7"/>
    <polygon points="0,0 73,0 256,166 256,518 0,292" fill="var(--sky)"/>
    <polygon points="0,292 256,518 256,549 0,549" fill="#ffffff"/>
    <polygon points="503,400 551,400 551,549 503,549" fill="var(--sky)"/>
  </svg>
  <div class="cover-title">
    <p class="kicker">NEW</p>
    <h1>BEAUTY<br>SALON</h1>
  </div>
  <p class="cover-intro">Treatments &amp; price list – facials, lashes, sugar-<br>ing, permanent make-up and airbrush tanning.</p>
  <div class="brand brand--cover"><span class="dot"></span>ATELIER KOVA</div>
</section>

<section class="page page--back">
  <div class="back-photo" role="img" aria-label="Blue-tinted close-up photo of a woman's face with hands framing it"></div>
  <svg class="shapes" viewBox="0 0 551 549" aria-hidden="true">
    <polygon points="0,0 238,0 0,214" fill="#ffffff" opacity="0.35"/>
    <polygon points="551,78 302,278 551,486" fill="#ffffff"/>
    <polygon points="0,326 236,549 0,549" fill="#ffffff" opacity="0.45"/>
  </svg>
  <p class="back-note">Quiet, personal care in the heart of Ixelles. Book your moment of calm at Atelier Kova and leave glowing.</p>
  <dl class="services">
    <dt>Gelaatsverzorging</dt>
    <dd>Classic facial 60 min € 65 · Deep-cleanse 75 min € 80</dd>
    <dt>Wimperverlenging</dt>
    <dd>Full set € 95 · Refill up to 3 weeks € 45</dd>
    <dt>Suikerontharing</dt>
    <dd>Lip or brows € 12 · Half legs € 30 · Full legs € 48</dd>
    <dt>Wimperlifting</dt>
    <dd>Lash lift with tint € 55 · With brow shape € 70</dd>
    <dt>Permanente Make Up</dt>
    <dd>Powder brows € 320 · Lip blush € 350 · Touch-up € 90</dd>
    <dt>Airbrush Tanning</dt>
    <dd>Full body € 35 · Package of five sessions € 150</dd>
  </dl>
  <div class="brand brand--back"><span class="dot"></span>ATELIER KOVA</div>
  <ul class="contact">
    <li class="phone">
      <svg viewBox="0 0 24 24"><path d="M6.6 10.8a15 15 0 0 0 6.6 6.6l2.2-2.2c.3-.3.7-.4 1-.2 1.1.4 2.3.6 3.6.6.6 0 1 .4 1 1V20c0 .6-.4 1-1 1A17 17 0 0 1 3 4c0-.6.4-1 1-1h3.5c.6 0 1 .4 1 1 0 1.3.2 2.5.6 3.6.1.3 0 .7-.2 1z"/></svg>
      02-6418 2275
    </li>
    <li>
      <svg viewBox="0 0 24 24"><path d="M2 5h20v14H2zm2 2v.5l8 5 8-5V7l-8 5z"/></svg>
      hello@atelierkova.be
    </li>
    <li>
      <svg viewBox="0 0 24 24"><path d="M12 2a10 10 0 1 0 0 20 10 10 0 0 0 0-20zm6.9 6h-2.9a15 15 0 0 0-1.4-3.9A8 8 0 0 1 18.9 8zM12 4c.8 1.2 1.5 2.5 1.9 4h-3.8c.4-1.5 1.1-2.8 1.9-4zM4.3 14a8 8 0 0 1 0-4h3.4a16 16 0 0 0 0 4zm.8 2h2.9c.3 1.4.8 2.7 1.4 3.9A8 8 0 0 1 5.1 16zM8 8H5.1a8 8 0 0 1 4.3-3.9C8.8 5.3 8.3 6.6 8 8zm4 12c-.8-1.2-1.5-2.5-1.9-4h3.8c-.4 1.5-1.1 2.8-1.9 4zm2.3-6H9.7a14 14 0 0 1 0-4h4.6a14 14 0 0 1 0 4zm.3 5.9c.6-1.2 1.1-2.5 1.4-3.9h2.9a8 8 0 0 1-4.3 3.9zM16.3 14a16 16 0 0 0 0-4h3.4a8 8 0 0 1 0 4z"/></svg>
      www.atelierkova.be
    </li>
    <li>
      <svg viewBox="0 0 24 24"><path d="M12 2a6 6 0 0 0-6 6c0 4.5 6 10 6 10s6-5.5 6-10a6 6 0 0 0-6-6zm0 8.5A2.5 2.5 0 1 1 12 5.5a2.5 2.5 0 0 1 0 5zM5 20h14v2H5z"/></svg>
      <span>Atelier Kova Studio:<br>Rue de la Vigne 14, Ixelles,<br>Brussels - 1050.</span>
    </li>
  </ul>
</section>

</body>
</html>
```